Brisk Nest - Business Card

Modern Business Card : I like a simple, clean designs. Think Quill!

Information to Include
Brisk Nest Inc. (Logo)
Name: Ted Marsh
Position: President
Office: 987-654-3210
Fax: 987-654-3210
Cell: 987-654-3210
E-Mail: tmarsh@thebrisknest.example
Website: www.thebrisknest.example

I attached the "gatebell.example" dealer logo. This logo is not a requirement, but a plus if it looks good with the design.

I also have access to more pictures and logos, if you see something on gatebell.example
or 7orb.example, I can probably get the file. Again, this is not mandatory.

```html
<!DOCTYPE html>
<html lang="en">
<head>
<meta charset="UTF-8">
<title>Brisk Nest – Business Card</title>
<link href="https://fonts.googleapis.com/css2?family=Roboto:wght@300;400;700&display=swap" rel="stylesheet">
<style>
  :root {
    --backdrop: #e4e2df;
    --card: #f4f4f3;
    --ink: #2b2b2b;
    --ink-soft: #555555;
    --accent: #d95a26;
    --shadow: rgba(0, 0, 0, 0.16);
  }
  * { margin: 0; padding: 0; box-sizing: border-box; }
  html, body {
    width: 1200px;
    height: 900px;
    overflow: hidden;
    background: var(--backdrop);
    font-family: "Roboto", Arial, sans-serif;
    color: var(--ink);
  }
  .canvas {
    width: 1200px;
    height: 900px;
    display: flex;
    flex-direction: column;
    align-items: center;
    justify-content: center;
    gap: 44px;
  }
  .card {
    position: relative;
    width: 600px;
    height: 343px;
    background: var(--card);
    box-shadow: 0 10px 26px var(--shadow), 0 2px 4px var(--shadow);
  }

  /* Front */
  .card-front {
    display: flex;
    align-items: center;
    justify-content: center;
  }
  .brand {
    display: flex;
    align-items: center;
    gap: 16px;
  }
  .brand-square {
    width: 22px;
    height: 22px;
    background: var(--accent);
  }
  .brand-name {
    font-weight: 700;
    font-size: 50px;
    letter-spacing: -0.5px;
    color: var(--accent);
  }

  /* Back */
  .card-back .brand {
    position: absolute;
    top: 34px;
    right: 40px;
    gap: 10px;
  }
  .card-back .brand-square { width: 14px; height: 14px; }
  .card-back .brand-name { font-size: 28px; }

  .dealer-badge {
    position: absolute;
    top: 100px;
    right: 44px;
    width: 74px;
    height: 58px;
    border: 2px solid var(--accent);
    border-radius: 10px;
  }

  .holder {
    position: absolute;
    left: 60px;
    top: 148px;
  }
  .holder-name {
    font-weight: 300;
    font-size: 25px;
    letter-spacing: 0.5px;
    text-transform: uppercase;
    color: var(--ink);
  }
  .holder-role {
    font-weight: 300;
    font-size: 15px;
    margin: 2px 0 0 18px;
    color: var(--ink-soft);
  }

  .contacts {
    position: absolute;
    left: 78px;
    top: 220px;
    list-style: none;
  }
  .contacts li {
    display: flex;
    align-items: center;
    gap: 12px;
    height: 21px;
    font-weight: 300;
    font-size: 15px;
    color: var(--ink);
  }
  .contact-icon {
    width: 14px;
    height: 14px;
    flex: none;
    color: var(--accent);
  }
  .contact-icon.at {
    font-weight: 400;
    font-size: 15px;
    line-height: 14px;
    text-align: center;
  }
</style>
</head>
<body>
<main class="canvas">

  <section class="card card-front" aria-label="Card front">
    <div class="brand">
      <span class="brand-square"></span>
      <span class="brand-name">Brisk Nest</span>
    </div>
  </section>

  <section class="card card-back" aria-label="Card back">
    <div class="brand">
      <span class="brand-square"></span>
      <span class="brand-name">Brisk Nest</span>
    </div>

    <div class="dealer-badge" role="img" aria-label="gatebell.example authorized dealer badge"></div>

    <div class="holder">
      <p class="holder-name">Ted Marsh</p>
      <p class="holder-role">President</p>
    </div>

    <ul class="contacts">
      <li>
        <svg class="contact-icon" viewBox="0 0 16 16" aria-label="Office"><path fill="currentColor" d="M2 5c0-2 2-3 6-3s6 1 6 3l-1 2-3-1V4.5H6V6L3 7z M4 9h8l1 5H3z"/></svg>
        987-654-3210
      </li>
      <li>
        <svg class="contact-icon" viewBox="0 0 16 16" aria-label="Fax"><path fill="currentColor" d="M4 1h6l2 2v3H4z M1 6h14v8H1z"/><rect x="4" y="9" width="8" height="2" fill="#f4f4f3"/></svg>
        987-654-3210
      </li>
      <li>
        <svg class="contact-icon" viewBox="0 0 16 16" aria-label="Cell"><rect x="2" y="3" width="12" height="10" rx="1.5" fill="none" stroke="currentColor" stroke-width="2"/></svg>
        987-654-3210
      </li>
      <li>
        <span class="contact-icon at" aria-label="E-mail">@</span>
        tmarsh@thebrisknest.example
      </li>
      <li>
        <svg class="contact-icon" viewBox="0 0 16 16" aria-label="Website"><rect x="4" y="2" width="8" height="12" rx="4" fill="none" stroke="currentColor" stroke-width="1.8"/><line x1="8" y1="3" x2="8" y2="7" stroke="currentColor" stroke-width="1.8"/></svg>
        www.thebrisknest.example
      </li>
    </ul>
  </section>

</main>
</body>
</html>
```